New Business Card Design Project

I have a logo I would like to use on the business card. I want something that will stand out and that will be remembered.

Target Market(s)

People who collect gems, minerals and crystals.

Contact Information for Business Card

email - mkthestonefalcon@vendrollo.com
phone # 917-406-2581

Font styles to use
Serif
Sans Serif
Decorative

Colors

Designer to choose colors to be used in the design.

Requirements
Must have
• The logo...two to choose from.
Nice to have
• An eye catching and memorable way to draw in people who collect gems minerals and crystals.

```html
<!DOCTYPE html>
<html lang="en">
<head>
<meta charset="utf-8">
<title>The Stone Falcon – Business Card</title>
<link rel="stylesheet" href="https://fonts.googleapis.com/css2?family=Alfa+Slab+One&family=Roboto:wght@400&family=Roboto+Condensed:wght@700&display=swap">
<style>
  :root {
    --royal: #2d419b;
    --paper: #ffffff;
    --ink: #0b0b0d;
    --silver: #c4c4c4;
    --stage: #ffffff;
  }
  * { box-sizing: border-box; margin: 0; padding: 0; }
  html, body {
    width: 1200px; height: 1200px; overflow: hidden;
    background: var(--stage);
    font-family: "Roboto", Arial, sans-serif;
  }
  .card {
    position: absolute; top: 229px;
    width: 420px; height: 720px;
    box-shadow: 0 14px 26px rgba(0,0,0,0.18);
  }
  .card--front {
    left: 152px; background: var(--paper);
    border: 6px solid var(--royal);
  }
  .card--back { left: 613px; background: var(--royal); }

  .brand {
    position: absolute; left: 0; right: 0;
    text-align: center;
  }
  .brand-name {
    font-family: "Alfa Slab One", Georgia, serif;
    font-weight: 400; text-transform: uppercase;
    line-height: 1; color: var(--ink);
  }
  .brand-tagline {
    font-family: "Roboto Condensed", Arial, sans-serif;
    font-weight: 700; text-transform: uppercase;
    white-space: nowrap;
  }
  .card--front .brand { top: 56px; }
  .card--front .brand-name { font-size: 36px; }
  .card--front .brand-tagline {
    margin-top: 10px; font-size: 12px; letter-spacing: 2px; color: var(--royal);
  }
  .card--back .brand { top: 416px; }
  .card--back .brand-name { font-size: 46px; }
  .card--back .brand-tagline {
    margin-top: 12px; font-size: 16px; letter-spacing: 2.4px; color: var(--silver);
  }

  .mascot { position: absolute; border-radius: 48% 48% 40% 40%; }
  .card--front .mascot {
    left: 62px; top: 215px; width: 284px; height: 294px;
    background: radial-gradient(ellipse at 50% 45%, #e6e6e6 0%, #c6c6c6 55%, #bdbdbd 100%);
    opacity: 0.9;
  }
  .card--back .mascot {
    left: 107px; top: 191px; width: 204px; height: 210px;
    background: radial-gradient(ellipse at 50% 50%, #6a6f80 0%, #15161b 60%, #0b0b0d 100%);
  }
  .ground {
    position: absolute; left: 58px; top: 403px;
    width: 304px; height: 5px; background: var(--ink);
    border-radius: 50%;
  }

  .contact {
    position: absolute; left: 0; right: 0; top: 585px;
    text-align: center; color: var(--ink);
    font-size: 19px; letter-spacing: 0.4px;
  }
  .contact-icons {
    display: flex; justify-content: center; align-items: center;
    gap: 7px; margin-bottom: 10px;
  }
  .contact-icons .divider { width: 1px; height: 20px; background: var(--ink); }
  .contact-line { line-height: 28px; }
</style>
</head>
<body>
  <section class="card card--front">
    <div class="brand">
      <h1 class="brand-name">The Stone<br>Falcon</h1>
      <p class="brand-tagline">Gems · Minerals · Crystals</p>
    </div>
    <div class="mascot" role="img" aria-label="Faint grey mascot illustration holding crystals with two pickaxes"></div>
    <div class="contact">
      <div class="contact-icons">
        <svg width="18" height="18" viewBox="0 0 24 24" aria-hidden="true">
          <path fill="#2d419b" d="M6.6 10.8a15.1 15.1 0 0 0 6.6 6.6l2.2-2.2c.3-.3.7-.4 1-.2 1.1.4 2.3.6 3.6.6.6 0 1 .4 1 1V20c0 .6-.4 1-1 1C10.6 21 3 13.4 3 4c0-.6.4-1 1-1h3.5c.6 0 1 .4 1 1 0 1.3.2 2.5.6 3.6.1.3 0 .7-.2 1z"/>
        </svg>
        <span class="divider"></span>
        <svg width="18" height="14" viewBox="0 0 24 18" aria-hidden="true">
          <rect x="0" y="0" width="24" height="18" rx="2" fill="#2d419b"/>
          <path d="M1 2l11 8 11-8" fill="none" stroke="#fff" stroke-width="2"/>
        </svg>
      </div>
      <p class="contact-line">917-406-2581</p>
      <p class="contact-line">mkthestonefalcon@vendrollo.com</p>
    </div>
  </section>

  <section class="card card--back">
    <div class="mascot" role="img" aria-label="Dark mascot illustration holding crystals with two crossed pickaxes"></div>
    <div class="ground"></div>
    <div class="brand">
      <h2 class="brand-name">The Stone<br>Falcon</h2>
      <p class="brand-tagline">Gems · Minerals · Crystals</p>
    </div>
  </section>
</body>
</html>
```